Website for data analytics startup

I have a landing page up at http://vantiq.io I need to expand this into a basic company website. I want something similar to this design: http://fetchlayout.com/samples/slider/

I need HTML and CSS for each of the designs, once they are approved. I need the following pages: home page, product, team, blog, and a design for the container of our demo application.

Our logo is attached and also available here: https://files.cloudvessel.com/vantiq.public/LOGO-colour.png I would like the website branding to match the logo.

I need a blog design with CSS that works with Pindle.

Our app can be seen at http://demo.vantiq.io Please don't change the look of the network graph itself, only the surrounding content.

For CSS, I want you to use Scaffolder or Groundwork as the starting point.

Target Market(s)

Sales and marketing, strategy

Industry/Entity Type

It Company

Coding

Coded - Design and coding required

Number of Pages Required

4 page

Font styles to use
Serif
Sans Serif

Requirements
Must have
• Clean, healthy appeal. Must work well with our logo. Blog page must integrate with Pindle easily. Must use Scaffolder or Groundwork for the starting point of the HTML/CSS.
Should not have
• Ugly crap, flash looking design. NO FLASH.

```html
<!DOCTYPE html>
<html lang="en">
<head>
<meta charset="utf-8">
<title>marqolo — Markets to Drive Sales and Marketing</title>
<link href="https://fonts.googleapis.com/css2?family=Open+Sans:wght@400;600;700&display=swap" rel="stylesheet">
<style>
:root{
  --green:#5aa83a;
  --teal:#1f5663;
  --text:#555;
  --muted:#888;
  --rule:#dcdcdc;
  --white:#fff;
  --footer:#1c1f22;
}
*{margin:0;padding:0;box-sizing:border-box}
html,body{width:717px;height:1200px;overflow:hidden}
body{position:relative;background:var(--white);font-family:"Open Sans",Arial,sans-serif;color:var(--text)}

.site-header{position:absolute;top:0;left:0;width:717px;height:67px;background:var(--white);display:flex;align-items:center;justify-content:space-between;padding:0 60px}
.brand{display:flex;align-items:center;gap:7px;color:var(--green);font-weight:700;font-size:22px;letter-spacing:.2px}
.brand-mark{width:12px;height:12px;background:var(--green)}
.main-nav{display:flex}
.main-nav a{font-size:9px;color:#444;text-decoration:none;padding:20px 11px 6px;border-top:2px solid transparent}
.main-nav a.active{color:var(--green);border-top-color:var(--green)}

.hero{position:absolute;top:67px;left:0;width:717px;height:311px;background:linear-gradient(100deg,#7d8d96 0%,#b9c4c9 35%,#8e9ea6 60%,#5d6c74 100%)}
.hero-copy{position:absolute;left:60px;top:100px;color:var(--white);font-size:27px;line-height:31px;font-weight:400}
.hero-copy .hero-brand{color:var(--green);font-weight:600}
.hero-arrows{position:absolute;right:26px;bottom:30px;display:flex;gap:5px}
.hero-arrows span{width:24px;height:22px;background:rgba(30,35,40,.55);display:flex;align-items:center;justify-content:center}

.section-title{position:absolute;left:0;width:717px;text-align:center;font-size:16px;font-weight:700;color:var(--teal);letter-spacing:.3px}
.section-title::after{content:"";display:block;width:36px;height:2px;background:var(--green);margin:7px auto 0}
.section-rule{position:absolute;left:60px;width:597px;height:1px;background:var(--rule)}

.welcome-text{position:absolute;left:60px;top:440px;width:597px;font-size:8px;line-height:13px;text-align:center;color:var(--text)}

.features{position:absolute;left:60px;top:478px;width:597px;display:flex;justify-content:space-between}
.feature{width:140px;text-align:center}
.feature-icon{width:62px;height:62px;border-radius:50%;background:var(--teal);margin:0 auto 12px;display:flex;align-items:center;justify-content:center;border:3px solid #cfdfe2;box-shadow:0 0 0 1px var(--teal)}
.feature h3{font-size:9px;font-weight:700;color:#333;margin-bottom:5px}
.feature p{font-size:7px;line-height:10px;color:var(--muted)}
.feature .read-more{display:inline-block;margin-top:6px;font-size:7px;color:#333;font-weight:600;text-decoration:none}

.projects{position:absolute;left:60px;top:734px;width:597px;display:flex;justify-content:space-between}
.project-thumb{width:143px;height:107px}
.thumb-1{background:linear-gradient(135deg,#cfe3ef,#6a9fc4)}
.thumb-2{background:linear-gradient(135deg,#e8ecef,#9fb2bf)}
.thumb-3{background:linear-gradient(135deg,#f2f2f2,#8c9399)}
.thumb-4{background:linear-gradient(135deg,#dfe6ea,#7f8f99)}

.testimonial{position:absolute;left:95px;top:962px;width:527px;font-size:7.5px;line-height:12px;text-align:center;color:var(--muted);font-style:italic}
.author{position:absolute;left:313px;top:1006px;display:flex;align-items:center;gap:10px}
.author-photo{width:44px;height:44px;border-radius:50%;background:linear-gradient(135deg,#c9c9c9,#7a7a7a)}
.author-name{font-size:10px;color:#333;font-weight:600}
.author-role{font-size:7px;color:var(--muted)}

.site-footer{position:absolute;top:1076px;left:0;width:717px;height:124px;background:linear-gradient(180deg,#2a2e32 0%,var(--footer) 60%,#121416 100%)}
.social{position:absolute;top:32px;left:0;width:717px;display:flex;justify-content:center;gap:6px}
.social span{width:19px;height:19px;border-radius:50%;background:var(--white)}
.footer-nav{position:absolute;top:70px;left:0;width:717px;display:flex;justify-content:center;gap:14px;font-size:8px;color:var(--white)}
.footer-nav a{color:var(--white);text-decoration:none}
.footer-nav .sep{color:#999}
.copyright{position:absolute;top:96px;left:0;width:717px;text-align:center;font-size:6.5px;color:#aaa}
</style>
</head>
<body>

<header class="site-header">
  <div class="brand"><span class="brand-mark"></span>marqolo</div>
  <nav class="main-nav">
    <a class="active" href="#">Home</a>
    <a href="#">About Us</a>
    <a href="#">Services</a>
    <a href="#">Market Network</a>
    <a href="#">Contact Us</a>
  </nav>
</header>

<section class="hero" role="img" aria-label="Blurred city skyline with a hand holding a smartphone showing a market network map">
  <h1 class="hero-copy"><span class="hero-brand">marqolo</span> Maps<br>Markets to Drive<br>Sales and Marketing</h1>
  <div class="hero-arrows">
    <span><svg width="8" height="10" viewBox="0 0 8 10"><path d="M6 1 2 5l4 4" stroke="#fff" stroke-width="1.6" fill="none"/></svg></span>
    <span><svg width="8" height="10" viewBox="0 0 8 10"><path d="M2 1l4 4-4 4" stroke="#fff" stroke-width="1.6" fill="none"/></svg></span>
  </div>
</section>

<h2 class="section-title" style="top:398px">WELCOME TO MARQOLO</h2>
<p class="welcome-text">Lorem ipsum dolor sit amet, consectetuer adipiscing elit. Aenean commodo ligula eget dolor. Aenean massa. Cum sociis natoque penatibus et magnis dis parturient montes, nascetur ridiculus mus. Donec quam felis, ultricies nec, pellentesque eu, pretium quis, sem. Nulla consequat massa quis enim.</p>

<div class="features">
  <div class="feature">
    <div class="feature-icon"><svg width="28" height="28" viewBox="0 0 28 28"><circle cx="14" cy="14" r="11" fill="#fff"/><path d="M14 14V3a11 11 0 0 1 11 11z" fill="#1f5663" stroke="#fff" stroke-width="1"/></svg></div>
    <h3>LOREM IPSUM DOLOR</h3>
    <p>Consectetuer adipiscing elit. Aenean commodo ligula eget dolor massa. Cum sociis natoque penatibus et magnis dis parturient.</p>
    <a class="read-more" href="#">Read More »</a>
  </div>
  <div class="feature">
    <div class="feature-icon"><svg width="28" height="28" viewBox="0 0 28 28"><rect x="4" y="16" width="4" height="8" fill="#fff"/><rect x="10" y="12" width="4" height="12" fill="#fff"/><rect x="16" y="8" width="4" height="16" fill="#fff"/><rect x="22" y="4" width="3" height="20" fill="#fff"/><path d="M3 24.5h23" stroke="#fff"/></svg></div>
    <h3>DOLOR SIT AMET</h3>
    <p>Consectetuer adipiscing elit. Aenean commodo ligula eget dolor massa. Cum sociis natoque penatibus et magnis dis parturient.</p>
    <a class="read-more" href="#">Read More »</a>
  </div>
  <div class="feature">
    <div class="feature-icon"><svg width="28" height="28" viewBox="0 0 28 28"><rect x="4" y="4" width="20" height="14" fill="none" stroke="#fff" stroke-width="2"/><path d="M7 15l4-4 3 3 6-6" stroke="#fff" stroke-width="1.6" fill="none"/><path d="M14 18v4M9 25l5-3 5 3" stroke="#fff" stroke-width="1.6" fill="none"/></svg></div>
    <h3>CONSECTETUER ADIPI</h3>
    <p>Consectetuer adipiscing elit. Aenean commodo ligula eget dolor massa. Cum sociis natoque penatibus et magnis dis parturient.</p>
    <a class="read-more" href="#">Read More »</a>
  </div>
  <div class="feature">
    <div class="feature-icon"><svg width="28" height="28" viewBox="0 0 28 28"><path d="M4 4v20h20" stroke="#fff" stroke-width="2" fill="none"/><path d="M7 20l5-6 4 3 7-9" stroke="#fff" stroke-width="2" fill="none"/></svg></div>
    <h3>AENEAN COMMODO</h3>
    <p>Consectetuer adipiscing elit. Aenean commodo ligula eget dolor massa. Cum sociis natoque penatibus et magnis dis parturient.</p>
    <a class="read-more" href="#">Read More »</a>
  </div>
</div>

<div class="section-rule" style="top:662px"></div>

<h2 class="section-title" style="top:685px">LATEST PROJECTS</h2>
<div class="projects">
  <div class="project-thumb thumb-1" role="img" aria-label="Tablet displaying business charts on a desk"></div>
  <div class="project-thumb thumb-2" role="img" aria-label="Hands writing over printed report graphs"></div>
  <div class="project-thumb thumb-3" role="img" aria-label="Business people walking in a bright office"></div>
  <div class="project-thumb thumb-4" role="img" aria-label="Laptop with analytics on a workspace"></div>
</div>

<div class="section-rule" style="top:885px"></div>

<h2 class="section-title" style="top:919px">CUSTOMER SATISFACTION</h2>
<p class="testimonial">“ Donec sapien aliquam at, ligula eget dolor consequat. Vivamus a velit eget arcu pretium convallis. Curabitur vitae augue et tellus aliquam blandit. Nam dapibus aliquam euismod ante nulla pellentesque tincidunt, quis aliquam felis adipiscing. ”</p>
<div class="author">
  <div class="author-photo" role="img" aria-label="Customer portrait"></div>
  <div><div class="author-name">Dana Whitfield</div><div class="author-role">Creative Designer</div></div>
</div>

<footer class="site-footer">
  <div class="social"><span></span><span></span><span></span><span></span><span></span><span></span><span></span></div>
  <nav class="footer-nav">
    <a href="#">Home</a><span class="sep">|</span>
    <a href="#">About Us</a><span class="sep">|</span>
    <a href="#">Services</a><span class="sep">|</span>
    <a href="#">Market Network</a><span class="sep">|</span>
    <a href="#">Contact Us</a>
  </nav>
  <p class="copyright">© Copy Rights 2015 marqolo.io | All Rights Reserved</p>
</footer>

</body>
</html>
```